business cards, stationary, email signature
Professional
Greta Volsky
President
Corporate office:
3620 E Tamsin Road, Orange, CA 92814
Other locations in Linden Bay, CA and Carver Falls, NV
greta@farwellgrp.net
www.farwellgrp.net
482650, K, D74
*8(a), *SDB, *SBE, *MBE, *DBE, *CBE
these certifications should be listed in the middle, bottom of the card.
■221119 – Other Electric Power Generation
■236210 – Industrial Building Construction
■236220 – Commercial and Institutional Building Construction
■237310 – Highway, Street, and Bridge Construction
■238160 – Roofing Contractors
■238170 – Siding Contractors
■238220 – Plumbing, Heating, and Air-Conditioning Contractors
■238310 – Drywall and Insulation Contractors
■238320 – Painting and Wall Covering Contractors
■238340 – Tile and Terrazzo Contractors
■238350 – Finish Carpentry Contractors
■238390 – Other Building Finishing Contractors
■238910 – Site Preparation Contractors
■238990 – All Other Specialty Trade Contractors
■541350 – Building Inspection Services
■561210 – Facilities Support Services
■561790 – Other Services to Buildings and Dwellings

```html
<!DOCTYPE html>
<html lang="en">
<head>
<meta charset="utf-8">
<title>Farwell Group – Business Card</title>
<link rel="stylesheet" href="https://fonts.googleapis.com/css2?family=Open+Sans:wght@400;600;700&display=swap">
<style>
  :root {
    --bg: #e9e6e1;
    --card: #ffffff;
    --ink: #555a5f;
    --blue: #2b84c6;
    --green-light: #8fb84a;
    --green-dark: #5e8a2c;
    --sky: #c9dcec;
    --sky-soft: #e6eef5;
  }
  * { margin: 0; padding: 0; box-sizing: border-box; }
  html, body { width: 1200px; height: 665px; overflow: hidden; background: var(--bg); }
  body { font-family: "Open Sans", Arial, sans-serif; color: var(--ink); position: relative; }

  .card {
    position: absolute; top: 178px; width: 540px; height: 310px;
    background: var(--card); overflow: hidden;
    box-shadow: 0 6px 18px rgba(0,0,0,.18);
  }
  .card--front { left: 40px; }
  .card--back { left: 620px; }
  .card__band { position: absolute; left: 0; top: 0; width: 540px; height: 310px; }

  /* front */
  .brand { position: absolute; left: 34px; top: 100px; display: flex; align-items: center; gap: 10px; }
  .brand__dot { width: 40px; height: 40px; border-radius: 50%; background: var(--blue); }
  .brand__name { font-size: 22px; font-weight: 600; color: var(--blue); letter-spacing: 1px; text-transform: uppercase; }
  .license { position: absolute; left: 84px; top: 136px; font-size: 8px; color: var(--blue); }

  .person { position: absolute; right: 30px; top: 28px; text-align: right; }
  .person__name { font-size: 12px; font-weight: 700; color: var(--ink); }
  .person__title { font-size: 8.5px; color: var(--ink); }

  .contact { position: absolute; right: 30px; top: 80px; text-align: right; font-size: 9px; line-height: 13px; color: var(--blue); list-style: none; }
  .contact li { display: flex; justify-content: flex-end; align-items: center; gap: 5px; }
  .contact__icon { width: 7px; height: 7px; background: var(--green-light); display: inline-block; }
  .contact__web { margin-top: 4px; }

  .office { position: absolute; left: 34px; top: 170px; font-size: 9px; line-height: 12px; color: var(--green-dark); }

  .certs { position: absolute; left: 0; right: 0; bottom: 14px; text-align: center; color: #fff; font-size: 9px; line-height: 12px; }

  /* back */
  .naics { position: absolute; left: 34px; top: 18px; list-style: none; font-size: 9px; line-height: 13.6px; color: var(--ink); }
  .naics li { display: flex; align-items: center; gap: 5px; }
  .naics li::before { content: ""; width: 6px; height: 6px; background: var(--blue); flex: none; }
  .skyline {
    position: absolute; right: 18px; bottom: 40px; width: 120px; height: 110px;
    background: linear-gradient(180deg, var(--sky-soft), var(--sky));
    border-radius: 4px 4px 0 0;
  }
  .back-brand { position: absolute; right: 26px; bottom: 12px; display: flex; align-items: center; gap: 7px; }
  .back-brand__dot { width: 16px; height: 16px; border-radius: 50%; background: #fff; }
  .back-brand__name { font-size: 13px; font-weight: 600; color: #fff; text-transform: uppercase; letter-spacing: 1px; }
</style>
</head>
<body>

<section class="card card--front">
  <svg class="card__band" viewBox="0 0 540 310" aria-hidden="true">
    <defs>
      <linearGradient id="frontBand" x1="0" y1="0" x2="1" y2="0">
        <stop offset="0" stop-color="#8fb84a"/>
        <stop offset="1" stop-color="#5e8a2c"/>
      </linearGradient>
    </defs>
    <path d="M0,258 C160,236 340,252 540,228 L540,310 L0,310 Z" fill="url(#frontBand)"/>
  </svg>

  <div class="brand">
    <span class="brand__dot"></span>
    <span class="brand__name">Farwell Group</span>
  </div>
  <p class="license">License # 482650, K, D74</p>

  <div class="person">
    <p class="person__name">Greta Volsky</p>
    <p class="person__title">President</p>
  </div>

  <ul class="contact">
    <li>(TF) 1.888.555.0142 <span class="contact__icon"></span></li>
    <li>1.714.555.0126 <span class="contact__icon"></span></li>
    <li>1.714.555.0183 <span class="contact__icon"></span></li>
    <li>1.714.555.0109 <span class="contact__icon"></span></li>
    <li class="contact__web">greta@farwellgrp.net</li>
    <li>www.farwellgrp.net</li>
  </ul>

  <div class="office">
    <p>Corporate office:</p>
    <p>3620 E Tamsin Road, Orange, CA 92814</p>
    <p>Other locations in Linden Bay, CA and Carver Falls, NV</p>
  </div>

  <div class="certs">
    <p>Certifications</p>
    <p>*8(a), *SDB, *SBE, *MBE, *DBE, *CBE</p>
  </div>
</section>

<section class="card card--back">
  <svg class="card__band" viewBox="0 0 540 310" aria-hidden="true">
    <defs>
      <linearGradient id="backBand" x1="0" y1="0" x2="1" y2="0">
        <stop offset="0" stop-color="#8fb84a"/>
        <stop offset="1" stop-color="#5e8a2c"/>
      </linearGradient>
    </defs>
    <path d="M0,284 C180,266 350,282 540,258 L540,310 L0,310 Z" fill="url(#backBand)"/>
  </svg>

  <div class="skyline" role="img" aria-label="Pale blue city skyline illustration"></div>

  <ul class="naics">
    <li>221119 – Other Electric Power Generation</li>
    <li>236210 – Industrial Building Construction</li>
    <li>236220 – Commercial and Institutional Building Construction</li>
    <li>237310 – Highway, Street, and Bridge Construction</li>
    <li>238160 – Roofing Contractors</li>
    <li>238170 – Siding Contractors</li>
    <li>238220 – Plumbing, Heating, and Air-Conditioning Contractors</li>
    <li>238310 – Drywall and Insulation Contractors</li>
    <li>238320 – Painting and Wall Covering Contractors</li>
    <li>238340 – Tile and Terrazzo Contractors</li>
    <li>238350 – Finish Carpentry Contractors</li>
    <li>238390 – Other Building Finishing Contractors</li>
    <li>238910 – Site Preparation Contractors</li>
    <li>238990 – All Other Specialty Trade Contractors</li>
    <li>541350 – Building Inspection Services</li>
    <li>561210 – Facilities Support Services</li>
    <li>561790 – Other Services to Buildings and Dwellings</li>
  </ul>

  <div class="back-brand">
    <span class="back-brand__dot"></span>
    <span class="back-brand__name">Farwell Group</span>
  </div>
</section>

</body>
</html>
```